Business card for IT company

Looking for a business card for an IT company providing server, network, and application support to medium businesses. Company name is Halvern Systems. Website is www.halvernsystems.example, would like to use the green color that is on the homepage. Prefer design to be done in Illustrator. Please, only DESIGNERS apply - no PHP programmers attempting to do design. Thank you

Industry/Entity Type

Information Technology

Requirements
Must have
• Green
Should not have
• Template designs, or designs done by non-designer type people

```html
<!DOCTYPE html>
<html lang="en">
<head>
<meta charset="utf-8">
<title>Halvern Systems – Business Card</title>
<link rel="stylesheet" href="https://fonts.googleapis.com/css2?family=Roboto:wght@400&display=swap">
<style>
  :root {
    --stage: #4b4b4b;
    --charcoal: #3f3f41;
    --green: #8dc641;
    --white: #ffffff;
  }
  * { box-sizing: border-box; margin: 0; padding: 0; }
  html, body {
    width: 1200px; height: 1200px; overflow: hidden;
    background: var(--stage);
    font-family: "Roboto", Arial, sans-serif;
  }
  .card {
    position: absolute; left: 247px;
    width: 705px; height: 400px;
    border-radius: 20px; overflow: hidden;
  }
  .card--front { top: 173px; background: var(--charcoal); }
  .card--back { top: 628px; background: var(--green); }

  .brand-band {
    position: absolute; left: 0; top: 100px;
    width: 313px; height: 199px; background: var(--green);
  }
  .divider {
    position: absolute; left: 313px; top: 67px;
    width: 1px; height: 264px; background: var(--green);
  }
  .brand-mark {
    position: absolute; border-radius: 50%; background: var(--white);
  }
  .brand-band .brand-mark { left: 110px; top: 22px; width: 90px; height: 90px; }
  .brand-name {
    position: absolute; left: 0; right: 0; text-align: center;
    color: var(--white); font-weight: 400; letter-spacing: 1px;
    text-transform: uppercase; line-height: 1.05;
  }
  .brand-band .brand-name { top: 124px; font-size: 19px; }

  .person {
    position: absolute; left: 340px; top: 118px;
    color: var(--white); font-size: 32px; font-weight: 400;
  }
  .contact-list { position: absolute; left: 340px; top: 169px; list-style: none; }
  .contact-list li {
    display: flex; align-items: center; height: 23.5px;
    color: var(--white); font-size: 18px;
  }
  .contact-list svg { width: 17px; height: 15px; margin-right: 13px; fill: var(--green); }
  .address {
    position: absolute; left: 340px; top: 255px;
    color: var(--white); font-size: 18px;
  }

  .card--back .brand-mark { left: 293px; top: 88px; width: 128px; height: 128px; }
  .card--back .brand-name { top: 232px; font-size: 34px; }
</style>
</head>
<body>

<section class="card card--front">
  <div class="brand-band">
    <div class="brand-mark"></div>
    <p class="brand-name">Halvern<br>Systems</p>
  </div>
  <div class="divider"></div>

  <h1 class="person">Dana Reyes</h1>
  <ul class="contact-list">
    <li>
      <svg viewBox="0 0 17 15" aria-hidden="true"><path d="M1 5c0-2 3-3 7.5-3S16 3 16 5v1h-3.5V4.5h-8V6H1z"/><path d="M3.5 7h10l1 7h-12z"/><circle cx="8.5" cy="10" r="1.8" fill="#3f3f41"/></svg>
      555.014.2290
    </li>
    <li>
      <svg viewBox="0 0 17 15" aria-hidden="true"><path d="M0 2h17v1.5L8.5 9 0 3.5z"/><path d="M0 5l8.5 5.5L17 5v8H0z"/></svg>
      support@halvernsystems.example
    </li>
    <li>
      <svg viewBox="0 0 17 15" aria-hidden="true"><path d="M8.5 0.5a7 7 0 1 0 0 14a7 7 0 1 0 0-14zm0 1.2c-1.2 1.3-1.9 3.4-1.9 5.8s.7 4.5 1.9 5.8c1.2-1.3 1.9-3.4 1.9-5.8S9.7 3 8.5 1.7zM2.7 6.9h11.6v1.2H2.7z" fill-rule="evenodd"/></svg>
      www.halvernsystems.example
    </li>
  </ul>
  <p class="address">Alder Ridge, CA</p>
</section>

<section class="card card--back">
  <div class="brand-mark"></div>
  <p class="brand-name">Halvern<br>Systems</p>
</section>

</body>
</html>
```